Scrap Metal Recycling

We are looking for a simple yet bold business card. We already have the logo, please see attached. Color scheme of blue, black and white or just blue and white.

```html
<!DOCTYPE html>
<html lang="en">
<head>
<meta charset="utf-8">
<title>R.K. Alloys Inc. – Business Card</title>
<link rel="stylesheet" href="https://fonts.googleapis.com/css2?family=Exo+2:wght@600;700&family=Open+Sans:wght@300;400;600&display=swap">
<style>
  :root {
    --charcoal: #3a3a3a;
    --ink: #333333;
    --brand-blue: #0a8db5;
    --card-white: #f4f4f4;
    --page-bg: #e6e6e6;
  }
  * { margin: 0; padding: 0; box-sizing: border-box; }
  html, body { width: 1200px; height: 900px; overflow: hidden; }
  body {
    background: var(--page-bg);
    font-family: "Open Sans", sans-serif;
    color: var(--ink);
    position: relative;
  }
  .business-card {
    position: absolute;
    left: 55px;
    top: 113px;
    width: 1090px;
    height: 673px;
    background: linear-gradient(180deg, #fafafa 0%, var(--card-white) 100%);
    box-shadow: 0 10px 30px rgba(0,0,0,0.15);
    overflow: hidden;
  }
  .card-shapes { position: absolute; inset: 0; width: 100%; height: 100%; }
  .brand-lockup {
    position: absolute;
    left: 0; width: 1094px;
    top: 262px;
    display: flex;
    justify-content: center;
    align-items: center;
    gap: 16px;
  }
  .brand-mark {
    width: 46px;
    height: 46px;
    border-radius: 50%;
    background: var(--brand-blue);
    flex: none;
  }
  .company-name {
    font-family: "Exo 2", sans-serif;
    font-weight: 700;
    font-size: 68px;
    line-height: 1;
    color: var(--charcoal);
    white-space: nowrap;
  }
  .tagline {
    position: absolute;
    left: 0; width: 1094px;
    top: 339px;
    text-align: center;
    font-weight: 600;
    font-size: 31px;
    letter-spacing: 0.32em;
    line-height: 1;
    color: var(--brand-blue);
    padding-left: 0.32em;
    white-space: nowrap;
  }
  .person-name {
    position: absolute;
    left: 0; width: 1094px;
    top: 412px;
    text-align: center;
    font-family: "Exo 2", sans-serif;
    font-weight: 700;
    font-size: 42px;
    line-height: 1;
    color: var(--ink);
  }
  .person-title {
    position: absolute;
    left: 0; width: 1094px;
    top: 454px;
    text-align: center;
    font-weight: 300;
    font-size: 31px;
    letter-spacing: -0.02em;
    line-height: 1;
    color: var(--brand-blue);
  }
  .address {
    position: absolute;
    right: 575px;
    top: 508px;
    text-align: right;
    font-style: normal;
    font-size: 29px;
    line-height: 39px;
    color: var(--ink);
    white-space: nowrap;
  }
  .divider {
    position: absolute;
    left: 545px;
    top: 515px;
    width: 2px;
    height: 108px;
    background: var(--ink);
  }
  .contact-list {
    position: absolute;
    left: 578px;
    top: 508px;
    list-style: none;
    font-size: 29px;
    line-height: 39px;
    color: var(--ink);
    white-space: nowrap;
  }
  .contact-list li { display: flex; align-items: center; gap: 12px; }
  .contact-icon { width: 30px; height: 30px; flex: none; }
</style>
</head>
<body>
  <div class="business-card">
    <svg class="card-shapes" viewBox="0 0 1090 673" aria-hidden="true">
      <path class="header-band" fill="#3a3a3a"
        d="M0 0 H1090 V330 C1040 210 820 140 540 137 C330 135 150 175 0 232 Z"/>
      <path class="header-swoosh" fill="#0a8db5"
        d="M0 232 C150 170 350 133 540 135 C820 138 1040 215 1090 325 C1110 385 1060 440 960 477 C1040 420 1055 360 1005 300 C925 212 755 160 540 152 C330 146 150 188 0 232 Z"/>
    </svg>

    <div class="brand-lockup">
      <span class="brand-mark" aria-hidden="true"></span>
      <span class="company-name">R.K. ALLOYS INC.</span>
    </div>
    <div class="tagline">SCRAP METAL RECYCLING</div>

    <div class="person-name">DANIEL HARPER</div>
    <div class="person-title">MANAGING DIRECTOR</div>

    <address class="address">
      88, Foundry Road<br>
      Eastgate Park<br>
      30817,Northland
    </address>

    <div class="divider"></div>

    <ul class="contact-list">
      <li>
        <svg class="contact-icon" viewBox="0 0 24 24" aria-hidden="true">
          <path fill="#0a8db5" d="M6.6 10.8c1.4 2.8 3.8 5.1 6.6 6.6l2.2-2.2c.3-.3.7-.4 1-.2 1.1.4 2.3.6 3.6.6.6 0 1 .4 1 1V20c0 .6-.4 1-1 1C10.6 21 3 13.4 3 4c0-.6.4-1 1-1h3.5c.6 0 1 .4 1 1 0 1.3.2 2.5.6 3.6.1.3 0 .7-.2 1z"/>
          <path fill="none" stroke="#0a8db5" stroke-width="1.6" d="M14 3a7 7 0 0 1 7 7M14 6.5a3.5 3.5 0 0 1 3.5 3.5"/>
        </svg>
        <span>044-987 654 321</span>
      </li>
      <li>
        <svg class="contact-icon" viewBox="0 0 24 24" aria-hidden="true">
          <rect x="2" y="5" width="20" height="14" fill="#0a8db5"/>
          <path d="M2 5 L12 13 L22 5 M2 19 L9.5 11 M22 19 L14.5 11" fill="none" stroke="#f4f4f4" stroke-width="1.4"/>
        </svg>
        <span>hello@rkalloys.com</span>
      </li>
      <li>
        <svg class="contact-icon" viewBox="0 0 24 24" aria-hidden="true">
          <g fill="none" stroke="#0a8db5" stroke-width="1.8">
            <circle cx="12" cy="12" r="10"/>
            <ellipse cx="12" cy="12" rx="4.5" ry="10"/>
            <path d="M2 12 H22 M4 6.5 H20 M4 17.5 H20"/>
          </g>
        </svg>
        <span>www.rkalloys.com</span>
      </li>
    </ul>
  </div>
</body>
</html>
```